IT company website design

Require a home page and an inner page designed for a company located in Ohio. The company deals with a wide range of IT services like Software development, IT based education services such as digital textbooks and BPO

Would like to get a Home page for the website and an inner page to be designed.

Design must be modern, clean and very professional. The home page should have a carousel of our services for which content will be provided.

It should give a feel that we are a large company to our prospective customers.
Updates

Hi,
In the few designs I have got for the home page, there are mockups with unwanted content/blocks like ex. latest blog posts or similar blocks. Kindly note that, we don't want this. Please follow the information about content on the home page as mentioned in the project brief. Designers, who have already submitted designs, if you can remove the unwanted blocks, it will be really appreciated.

Thanks.

I have received over 9 designs for this project, but none of them seem to be custom designed for my needs. They are just re-use of previous designs and look very out dated. Looking for fresh, clean designs following latest design trends like the ones you see in pixelbazaar etc.

If you can provide me a design that meets my expectations, I can definitely UP my budget for you .

Industry/Entity Type

Education

Requirements
Must have
• > > Home page > >
Home page will have

* Top Menu: Home, About Us, Solutions, Services, Contact us (should have space to accommodate for more)

* Should have a flash carousel/slide show. Each slide should be about a service we provide. Ex. a slide for bpo will have the content "Bridging the quality and cost divide in outsourcing" It should be depicted by an illustration or photograph. If you are going to use photograph, please use ones for framelode.com

* Textual content of about 200 words which we will provide

* Links in the footer along with a copyright, legal notice etc.

* Importantly, the home page should have 2 fancy buttons for "Member Login" and "Online Tutoring"

> > Inner pages > >
Will be mainly textual content explaining each of the service so, should have space for lots of textual content, with a fancy, page title (usually the service name). All inner pages should also have a side menu or something like that from where users can have a one click access to all our services.

Our logo is blue in color. with color code "0080FB". It just a stylized D with rest of the text i.e Quorvane Tech Inc. our logo is of the proportion. 1:5 i.e 60px height, 300px wide. We can proportionately increase or decrease the dimensions as necessary. Color combination of the sight should be something that will go with this.

```html
<!DOCTYPE html>
<html lang="en">
<head>
<meta charset="utf-8">
<title>Quorvane Tech, Inc — Home</title>
<link href="https://fonts.googleapis.com/css2?family=Open+Sans:wght@400;600&family=Jost:wght@500;600&family=Arimo&display=swap" rel="stylesheet">
<style>
  :root{
    --page:#f4f4f4;
    --sky-top:#cfe1ee;
    --sky-bottom:#74b5f3;
    --brand:#0080fb;
    --nav:#0b55a8;
    --orange:#ff8a1c;
    --orange-dark:#e56800;
    --headline-light:#2596cf;
    --headline-dark:#3d6f8e;
    --heading:#1e8ae6;
    --body:#444;
    --footer:#cfe2ee;
  }
  *{margin:0;padding:0;box-sizing:border-box}
  html,body{width:1200px;height:1000px;overflow:hidden}
  body{background:var(--page);font-family:"Open Sans",sans-serif;position:relative}

  .sky{position:absolute;left:0;top:84px;width:1200px;height:400px;
    background:linear-gradient(var(--sky-top),#b8d6f0 45%,var(--sky-bottom))}
  .edge{position:absolute;left:0;width:1200px;height:12px;
    background:linear-gradient(135deg,var(--page) 50%,transparent 50%) 0 0/12px 12px,
               linear-gradient(225deg,var(--page) 50%,transparent 50%) 0 0/12px 12px}
  .sky .edge{top:0}

  .brand{position:absolute;left:144px;top:30px;display:flex;align-items:center;gap:12px}
  .brand-mark{width:28px;height:28px;background:var(--brand)}
  .brand-name{font-size:22px;font-weight:600;color:var(--brand)}

  .main-nav{position:absolute;top:0;left:563px;display:flex;list-style:none}
  .main-nav li{height:100px;padding-top:40px;font-size:16px;color:var(--nav);margin-right:48px}
  .main-nav li:last-child{margin-right:0}
  .main-nav .active{width:83px;height:118px;margin-right:30px;color:#fff;text-align:center;
    background:linear-gradient(var(--orange),var(--orange-dark));
    clip-path:polygon(0 0,100% 0,100% 100%,50% 94%,0 100%)}

  .quick-btn{position:absolute;top:122px;height:40px;border-radius:5px;
    background:linear-gradient(#f3f9fd,#cfe6f7);border:1px solid #a9cbe6;
    display:flex;align-items:center;gap:8px;padding-left:4px;font-size:16px;color:#333}
  .quick-btn .icon{width:32px;height:32px;border-radius:3px;background:linear-gradient(#ff9b34,var(--orange-dark));
    display:flex;align-items:center;justify-content:center}
  .login{left:747px;width:163px}
  .tutoring{left:921px;width:163px}

  .carousel{position:absolute;left:128px;top:192px;width:954px;height:420px;background:#fff;
    box-shadow:0 1px 5px rgba(0,0,0,.25);padding:9px}
  .slide{position:relative;width:936px;height:402px;background:#e8f6fd;overflow:hidden}
  .slide-photo{position:absolute;left:375px;top:0;width:561px;height:402px;
    background:linear-gradient(90deg,#e8f6fd,#cfdbe4 30%,#e9eef2 60%,#f4f4f2)}
  .slide-title{position:absolute;left:65px;top:96px;font-family:"Jost",sans-serif;font-weight:600;
    line-height:.95;text-transform:uppercase;letter-spacing:-.5px}
  .slide-title span{display:block}
  .t1{font-size:72px;color:var(--headline-light)}
  .t2{font-size:56px;color:var(--headline-dark)}
  .t3{font-size:48px;color:var(--headline-dark)}
  .t4{font-size:40px;color:var(--headline-light)}
  .arrow{position:absolute;top:172px}
  .prev{left:10px}.next{right:18px}
  .dots{position:absolute;left:451px;top:376px;display:flex;gap:7px}
  .dots i{width:8px;height:8px;border-radius:50%;background:#999}
  .dots i:first-child{background:#555}

  .intro{position:absolute;left:131px;top:636px;width:950px;color:var(--body)}
  .intro h1{font-weight:400;font-size:25px;color:var(--heading);margin-bottom:6px}
  .intro p{font-size:13.6px;line-height:18px;margin-bottom:18px;text-align:justify}

  .site-footer{position:absolute;left:0;top:918px;width:1200px;height:82px;
    background:linear-gradient(#e6eff5,var(--footer) 30%)}
  .site-footer .edge{top:0}
  .footer-nav,.legal{position:absolute;left:134px;font-family:"Arimo",sans-serif;color:#111}
  .footer-nav{top:26px;font-size:12px;word-spacing:2px}
  .legal{top:51px;font-size:11px}
  .legal a{color:#0a66d8;margin:0 3px}
</style>
</head>
<body>
  <div class="sky"><div class="edge"></div></div>

  <header>
    <div class="brand"><span class="brand-mark"></span><span class="brand-name">Quorvane Tech, Inc</span></div>
    <ul class="main-nav">
      <li class="active">Home</li>
      <li>About Us</li>
      <li>Solutions</li>
      <li>Services</li>
      <li>Contact us</li>
    </ul>
    <a class="quick-btn login"><span class="icon">
      <svg width="22" height="22" viewBox="0 0 22 22"><path d="M8 2h12v18H8" fill="none" stroke="#fff" stroke-width="2.4"/><path d="M15 11H3M8 6l-5 5 5 5" fill="none" stroke="#fff" stroke-width="2.4"/></svg>
    </span>Member Login</a>
    <a class="quick-btn tutoring"><span class="icon">
      <svg width="22" height="22" viewBox="0 0 22 22"><rect x="2" y="3" width="18" height="12" fill="none" stroke="#fff" stroke-width="2.4"/><path d="M7 19h8M11 15v4" stroke="#fff" stroke-width="2.4"/></svg>
    </span>Online Tutoring</a>
  </header>

  <section class="carousel">
    <div class="slide">
      <div class="slide-photo" role="img" aria-label="Photo of a smiling customer support team wearing headsets"></div>
      <h2 class="slide-title">
        <span class="t1">Bridging</span>
        <span class="t2">The Quality</span>
        <span class="t3">&amp; Cost Divide</span>
        <span class="t4">In Outsourcing</span>
      </h2>
      <svg class="arrow prev" width="28" height="40" viewBox="0 0 28 40"><path d="M22 4L6 20l16 16" fill="none" stroke="#111" stroke-width="6"/></svg>
      <svg class="arrow next" width="28" height="40" viewBox="0 0 28 40"><path d="M6 4l16 16L6 36" fill="none" stroke="#111" stroke-width="6"/></svg>
      <div class="dots"><i></i><i></i><i></i><i></i><i></i></div>
    </div>
  </section>

  <main class="intro">
    <h1>Aenean nec libero ante</h1>
    <p>Lorem ipsum dolor sit amet, consectetur adipiscing elit. Ut in lorem erat, eu convallis arcu. Praesent ligula est, semper a congue vitae, dignissim a orci. Proin condimentum euismod nulla, vitae laoreet justo tempor tincidunt. Vestibulum nec malesuada ligula. Cras sodales eros ac nisi ornare dignissim. In gravida elit at mi viverra nec malesuada arcu auctor.</p>
    <p>Duis posuere vulputate nisl, ac molestie risus cursus vitae. Integer convallis lectus eros, non dapibus magna. Aliquam placerat, nibh at tincidunt commodo, orci ante semper orci, et cursus mauris nunc quis nisi. Etiam in nibh nec orci tempor semper. Maecenas est erat, tincidunt sit amet elementum sed, porta id risus. Praesent malesuada tristique porttitor. Etiam venenatis ultrices arcu, id condimentum orci semper eu. Nulla facilisi. Sed a leo velit, ac auctor sapien. Mauris massa nisl, aliquet sed pellentesque et, venenatis at tortor. Curabitur id ligula nisl. Sed sed diam nisi. Nullam laoreet tristique turpis quis fringilla.</p>
    <p>Donec fermentum commodo quam id gravida. Sed ac metus ac nisl aliquam iaculis eget in ipsum. Quisque consequat orci felis, sed faucibus sapien. Nulla vehicula, leo vestibulum pharetra pharetra, ante mi ultrices justo, eu dictum odio diam vel turpis. Quisque interdum, dolor quis pharetra congue, ante risus bibendum tellus</p>
  </main>

  <footer class="site-footer">
    <div class="edge"></div>
    <nav class="footer-nav">Home &nbsp;| &nbsp;About Us &nbsp;| &nbsp;Solutions &nbsp;| &nbsp;Services &nbsp;| &nbsp;Contact us</nav>
    <p class="legal">copyright 2011 Quorvane Tech Inc. All rights reserved. <a>Privacy Policy</a>|<a>Terms and Policies</a></p>
  </footer>
</body>
</html>
```